Communications & Broadcast Consulting/PR/Media Relations & Public Affairs

My main goals are to provide communications support to school districts, small towns/cities/hospitals and private businesses in the form of press releases, media relations, public affairs. I also have 25 years experience as a television news anchor/reporter and I'm open to free-lance reporting in both Indianapolis and other markets. My specialty is working with the media.
Communications

```html
<!DOCTYPE html>
<html lang="en">
<head>
<meta charset="utf-8">
<title>Ridgeway Communications – Business Card</title>
<link rel="stylesheet" href="https://fonts.googleapis.com/css2?family=Oswald:wght@500&family=Mulish:wght@400;700&display=swap">
<style>
  :root {
    --page-bg: #eceeee;
    --brand-blue: #0f5a9c;
    --brand-blue-deep: #0a3f78;
    --brand-blue-light: #3f8fd0;
    --silver-light: #ffffff;
    --silver-mid: #d9dadb;
    --silver-dark: #a9abad;
    --ink: #2f3236;
    --icon-blue: #2a5a8e;
  }
  html, body {
    margin: 0;
    padding: 0;
    width: 853px;
    height: 1200px;
    overflow: hidden;
    background: var(--page-bg);
  }
  .card {
    position: absolute;
    left: 119px;
    top: 108px;
    width: 583px;
    height: 982px;
    overflow: hidden;
    font-family: "Mulish", "Century Gothic", sans-serif;
  }
  .card-art {
    position: absolute;
    inset: 0;
    width: 583px;
    height: 982px;
  }
  .company-name {
    position: absolute;
    top: 34px;
    left: 0;
    width: 583px;
    margin: 0;
    text-align: center;
    font-family: "Oswald", "Arial Narrow", sans-serif;
    font-weight: 500;
    font-size: 55px;
    line-height: 1;
    color: #ffffff;
    letter-spacing: 0.2px;
  }
  .person {
    position: absolute;
    top: 205px;
    left: 0;
    width: 583px;
    text-align: center;
  }
  .person-name {
    margin: 0;
    font-weight: 700;
    font-size: 29px;
    color: var(--brand-blue);
  }
  .person-role {
    margin: 6px 0 0;
    font-size: 26px;
    color: var(--ink);
  }
  .contact-list {
    position: absolute;
    top: 305px;
    left: 68px;
    margin: 0;
    padding: 0;
    list-style: none;
    font-size: 27px;
    color: var(--ink);
  }
  .contact-item {
    display: flex;
    align-items: flex-start;
    gap: 8px;
    height: 48px;
  }
  .contact-item svg {
    flex: none;
    width: 26px;
    height: 26px;
    margin-top: 5px;
  }
  .contact-address {
    line-height: 1.35;
    font-size: 25px;
  }
  .tower-illustration {
    position: absolute;
    left: 182px;
    top: 530px;
    width: 222px;
    height: 430px;
    border-radius: 110px 110px 8px 8px;
    background: linear-gradient(180deg, rgba(63,143,208,0.35) 0%, rgba(15,90,156,0.55) 55%, rgba(63,143,208,0.4) 100%);
  }
</style>
</head>
<body>
  <div class="card">
    <svg class="card-art" viewBox="0 0 583 982" aria-hidden="true">
      <defs>
        <linearGradient id="silverSheet" x1="0" y1="0" x2="1" y2="0">
          <stop offset="0" stop-color="#c9cacc"/>
          <stop offset="0.3" stop-color="#f4f4f5"/>
          <stop offset="0.55" stop-color="#ffffff"/>
          <stop offset="0.8" stop-color="#ebebec"/>
          <stop offset="1" stop-color="#bfc1c3"/>
        </linearGradient>
        <linearGradient id="headerBlue" x1="0" y1="0" x2="0" y2="1">
          <stop offset="0" stop-color="#0a3f78"/>
          <stop offset="0.55" stop-color="#0f5a9c"/>
          <stop offset="1" stop-color="#3f8fd0"/>
        </linearGradient>
        <linearGradient id="silverBand" x1="0" y1="0" x2="1" y2="0">
          <stop offset="0" stop-color="#8f9194"/>
          <stop offset="0.35" stop-color="#ffffff"/>
          <stop offset="0.65" stop-color="#d5d6d8"/>
          <stop offset="1" stop-color="#8f9194"/>
        </linearGradient>
      </defs>
      <rect class="card-sheet" width="583" height="982" fill="url(#silverSheet)"/>
      <path class="header-band-edge" d="M0 0 H583 V146 Q291 196 0 146 Z" fill="url(#silverBand)"/>
      <path class="header-band" d="M0 0 H583 V132 Q291 178 0 132 Z" fill="url(#headerBlue)"/>
      <path class="footer-band" d="M0 950 Q291 905 583 950 V982 H0 Z" fill="url(#silverBand)"/>
    </svg>

    <h1 class="company-name">Ridgeway Communications</h1>

    <div class="person">
      <p class="person-name">Dale Ridgeway</p>
      <p class="person-role">Public &amp; Media Relations Consultant</p>
    </div>

    <ul class="contact-list">
      <li class="contact-item">
        <svg viewBox="0 0 24 24" aria-label="Phone"><path d="M6.5 3 L9.5 3 L10.5 8 L8.3 9.6 Q10 13.8 14.4 15.7 L16 13.5 L21 14.5 L21 17.5 Q20.5 21 17 21 Q4 19.5 3 7 Q3 3.5 6.5 3 Z" fill="var(--icon-blue)"/></svg>
        <span>317 555 0142</span>
      </li>
      <li class="contact-item">
        <svg viewBox="0 0 24 24" aria-label="Mobile"><rect x="6" y="2" width="12" height="20" rx="2" fill="none" stroke="var(--icon-blue)" stroke-width="1.8"/><line x1="10" y1="18.5" x2="14" y2="18.5" stroke="var(--icon-blue)" stroke-width="1.6"/></svg>
        <span>317 555 0187</span>
      </li>
      <li class="contact-item">
        <svg viewBox="0 0 24 24" aria-label="Email"><rect x="2" y="6" width="20" height="13" fill="none" stroke="var(--icon-blue)" stroke-width="1.8"/><path d="M2 6 L12 14 L22 6" fill="none" stroke="var(--icon-blue)" stroke-width="1.8"/></svg>
        <span>dridgeway77@mailbox.net</span>
      </li>
      <li class="contact-item">
        <svg viewBox="0 0 24 24" aria-label="Address"><path d="M1 10 L12 3 L23 10 Z" fill="var(--icon-blue)"/><rect x="3" y="11" width="18" height="10" fill="var(--icon-blue)"/><rect x="6" y="13" width="4" height="4" fill="#ffffff"/><rect x="14" y="13" width="4" height="4" fill="#ffffff"/></svg>
        <span class="contact-address">2218 Alder Court Indianapolis,<br>IN 46201</span>
      </li>
    </ul>

    <div class="tower-illustration" role="img" aria-label="Illustration of a broadcast transmission tower sending signal waves"></div>
  </div>
</body>
</html>
```